Design Only - Custom Travel Brand E-Commerce *

I have a basic website layout already made on Shopify, but looking for some additional design touches on a few pages. We would like to add some more style and creativity to the site. The images on the site are not final, just placeholders.

We are a travel brand selling our first 2 items (custom luggage tag & passport wallet). The premise is to engrave the product with everywhere you have been and everywhere you will go. You are allowed to ship back to us and re-engrave new places for $5.

The customizer page is already coded but we can make changes to the forms (select countries, enter contact information form, and overall flow)

Target Market(s)

Millennials and travelers. Most likely more females then males will be purchasing. Also for parents buying children gift cards/gifts

Industry/Entity Type

E-Commerce

Number of Pages Required

5+ page

Font styles to use
Sans Serif

Colors
85cae6
3176b5
acd136

Requirements
Must have
• Looking for ways to add some new design to the pages. It's a new product category so want the customer to fully understand what it is and how it works. The gifting page will be important because you can either buy a blank tag/passport holder as a gift ($5 paid one-time return included) or a gift card from the gifting page.
Nice to have
• Looking to add a bit of color. Gray is ok. Brand is primarily black and white but would be nice to add a TINY pop of color on certain buttons maybe.
Should not have
• The customizer feature is fixed. You can change the form look/feel.

```html
<!DOCTYPE html>
<html lang="en">
<head>
<meta charset="utf-8">
<title>Roamstead – Passport Wallet</title>
<link rel="stylesheet" href="https://fonts.googleapis.com/css2?family=Roboto:wght@300;400;500;700;900&display=swap">
<style>
:root{
  --sky:#85cae6;
  --blue:#3176b5;
  --lime:#acd136;
  --ink:#1b1b1b;
  --text:#555;
  --muted:#999;
  --line:#e3e3e3;
  --grey-band:#efefef;
  --footer:#0c0c0c;
  --white:#fff;
}
*{box-sizing:border-box;margin:0;padding:0}
html,body{width:1200px;height:3312px;overflow:hidden}
body{font-family:"Roboto",Arial,sans-serif;color:var(--ink);background:var(--white);position:relative}
.abs{position:absolute}
a{color:inherit;text-decoration:none}

/* top strip */
.promo-strip{left:0;top:0;width:1200px;height:40px;background:var(--sky);color:var(--white);font-size:13px;display:flex;align-items:center;justify-content:center;letter-spacing:.5px}

/* header */
.site-header{left:0;top:40px;width:1200px;height:88px;border-bottom:1px solid var(--line)}
.main-nav{left:108px;top:34px;display:flex;gap:22px;font-size:11px;font-weight:500;letter-spacing:.6px;color:#333}
.brand-mark{left:488px;top:16px;width:224px;height:56px;border:2px solid var(--ink);display:flex;align-items:center;justify-content:center;font-size:28px;font-weight:500;letter-spacing:5px}
.header-tools{right:108px;top:32px;display:flex;gap:24px;font-size:11px;font-weight:500;letter-spacing:.6px;align-items:center}

/* hero */
.hero{left:0;top:128px;width:1200px;height:512px;background:linear-gradient(100deg,#3f9ed2 0%,#4aa7d8 45%,#5a6b78 70%,#2b2f33 100%)}
.hero-card{left:120px;top:228px;width:548px;height:228px;background:rgba(255,255,255,.86);padding:34px 34px}
.hero-title{font-size:50px;font-weight:700;letter-spacing:12px;color:#222;line-height:56px}
.hero-copy{margin-top:16px;width:430px;font-size:13px;line-height:19px;color:var(--text)}
.btn-sky{display:inline-block;background:var(--sky);color:var(--white);font-size:11px;font-weight:700;letter-spacing:1px;padding:11px 22px}
.hero-card .btn-sky{position:absolute;right:40px;bottom:26px}

/* product */
.product-photo{left:180px;top:690px;width:300px;height:520px;background:radial-gradient(ellipse at 50% 45%,#a9c1ea 0%,#8ea9dc 45%,#f4f6fb 72%,#fff 100%)}
.product-info{left:600px;top:724px;width:490px}
.product-title{font-size:26px;font-weight:400;letter-spacing:1px}
.product-title b{font-weight:700}
.product-copy{margin-top:12px;font-size:13px;line-height:19px;color:var(--muted)}
.product-info .btn-sky{margin-top:16px}
.price{margin-top:22px;font-size:26px;font-weight:500;padding-bottom:16px;border-bottom:1px solid var(--line)}
.option-labels{margin-top:16px;display:flex;gap:14px;font-size:10px;font-weight:700;letter-spacing:1px}
.swatches{margin-top:12px;display:flex;gap:8px}
.swatch{width:18px;height:18px;border-radius:50%}
.btn-block{display:block;width:490px;height:50px;line-height:50px;text-align:center;color:var(--white);font-size:12px;font-weight:700;letter-spacing:1.5px}
.btn-customize{margin-top:22px;background:var(--blue)}
.btn-gift{margin-top:20px;background:var(--lime)}
.share-row{margin-top:30px;display:flex;justify-content:center;gap:10px}
.share-dot{width:14px;height:14px;border-radius:50%;background:#999}

/* testimonials */
.testimonials{left:0;top:1310px;width:1200px;height:480px;background:var(--grey-band)}
.section-title{width:1200px;text-align:center;font-size:30px;font-weight:400;letter-spacing:1px;line-height:36px}
.section-title b{font-weight:900}
.testimonials .section-title{top:76px}
.rule{left:575px;width:50px;height:3px;background:#333}
.avatar{left:552px;top:148px;width:96px;height:96px;border-radius:50%;background:linear-gradient(#c9b39a,#8a6f55);border:4px solid var(--white)}
.quote{left:230px;top:262px;width:740px;text-align:center;font-size:13px;line-height:20px;color:var(--muted)}
.quote-name{left:0;top:358px;width:1200px;text-align:center;font-size:12px;font-weight:700;letter-spacing:1px}
.quote-role{left:0;top:378px;width:1200px;text-align:center;font-size:10px;font-weight:700;letter-spacing:1px;color:var(--lime)}
.arrow{top:270px;width:24px;height:40px}

/* tiles */
.tile{overflow:hidden}
.tile-label{position:absolute;left:56px;bottom:38px;color:var(--white);font-size:32px;font-weight:400;letter-spacing:1px}
.tile-label b{font-weight:900}
.tile-luggage{left:12px;top:1800px;width:716px;height:336px;background:linear-gradient(120deg,#9aa3ab 0%,#6f7780 50%,#3d434a 100%)}
.tile-sale{left:744px;top:1800px;width:444px;height:336px;background:var(--lime);color:var(--white);text-align:center;padding-top:68px}
.sale-title{font-size:34px;font-weight:700}
.sale-rule{width:64px;height:3px;background:var(--white);margin:18px auto 0}
.sale-copy{width:300px;margin:20px auto 0;font-size:13px;line-height:19px}
.btn-blue{display:inline-block;margin-top:30px;background:var(--blue);color:var(--white);font-size:11px;font-weight:700;letter-spacing:1px;padding:15px 40px}
.tile-wallet-a{left:12px;top:2148px;width:584px;height:332px;background:linear-gradient(135deg,#5a4333 0%,#7a2f2a 45%,#2f2620 100%)}
.tile-wallet-b{left:604px;top:2148px;width:584px;height:332px;background:linear-gradient(135deg,#6b5a44 0%,#cdb48b 45%,#4a3b2d 100%)}

/* related */
.related .section-title{top:2566px}
.related-card{top:2630px;width:316px;text-align:center}
.related-photo{width:316px;height:196px}
.related-name{margin-top:24px;font-size:14px;font-weight:700;letter-spacing:1px}
.related-price{margin-top:6px;font-size:22px;font-weight:500;color:var(--blue)}

/* footer */
.site-footer{left:0;top:2995px;width:1200px;height:317px;background:var(--footer);color:#bbb}
.footer-col{top:60px;width:200px;font-size:11px;line-height:20px}
.footer-col h4{color:var(--white);font-size:12px;font-weight:700;letter-spacing:1px;margin-bottom:14px}
.footer-bottom{left:108px;top:254px;width:984px;display:flex;align-items:center;justify-content:space-between;font-size:11px}
.cards{display:flex;gap:8px}
.card-chip{width:34px;height:22px;background:#e8e8e8;border-radius:3px}
</style>
</head>
<body>

<div class="abs promo-strip">Free shipping on orders over $50</div>

<header class="abs site-header">
  <nav class="abs main-nav"><a>SHOP</a><a>SETTING</a><a>ABOUT US</a><a>REGISTER YOUR TAG</a></nav>
  <div class="abs brand-mark">ROAMSTEAD</div>
  <div class="abs header-tools">
    <span>USD ▾</span><span>CART (0)</span>
    <svg width="14" height="14" viewBox="0 0 14 14"><circle cx="6" cy="6" r="4.5" fill="none" stroke="#222" stroke-width="1.6"/><line x1="9.3" y1="9.3" x2="13" y2="13" stroke="#222" stroke-width="1.6"/></svg>
  </div>
</header>

<section class="abs hero" role="img" aria-label="Travel bag with luggage tag and passport on a blue wooden table"></section>
<div class="abs hero-card">
  <h1 class="hero-title">ROAMSTEAD</h1>
  <p class="hero-copy">Set out with a tag that remembers every place you have been and every place you will go next.</p>
  <a class="btn-sky">SHOP NOW</a>
</div>

<div class="abs product-photo" role="img" aria-label="Light blue passport wallet with strap"></div>
<section class="abs product-info">
  <h2 class="product-title"><b>ROAMSTEAD</b> PASSPORT WALLET</h2>
  <p class="product-copy">Engrave every country you have visited on a slim leather wallet, then send it back to add new places for five dollars.</p>
  <a class="btn-sky">LEARN MORE</a>
  <div class="price">$ 35.00</div>
  <div class="option-labels"><span>COLOR</span><span style="color:#ccc">|</span><span>SIZE</span></div>
  <div class="swatches">
    <span class="swatch" style="background:#e8c07a;outline:2px solid #ddd;outline-offset:2px"></span>
    <span class="swatch" style="background:#9fb6e3"></span>
    <span class="swatch" style="background:#b9c6dc"></span>
    <span class="swatch" style="background:#85cae6"></span>
  </div>
  <a class="btn-block btn-customize">CUSTOMIZE</a>
  <a class="btn-block btn-gift">BUY AS GIFT</a>
  <div class="share-row"><span class="share-dot"></span><span class="share-dot"></span><span class="share-dot"></span><span class="share-dot"></span><span class="share-dot"></span></div>
</section>

<section class="abs testimonials">
  <h2 class="abs section-title"><b>OUR</b> CUSTOMERS SAY</h2>
  <div class="abs rule" style="top:124px"></div>
  <div class="abs avatar" role="img" aria-label="Customer portrait"></div>
  <svg class="abs arrow" style="left:100px" viewBox="0 0 24 40"><polyline points="18,6 6,20 18,34" fill="none" stroke="#444" stroke-width="3"/></svg>
  <svg class="abs arrow" style="right:100px" viewBox="0 0 24 40"><polyline points="6,6 18,20 6,34" fill="none" stroke="#444" stroke-width="3"/></svg>
  <p class="abs quote">Our first trip with the engraved tag felt special. Every airport we passed through made us smile, and the tag now holds a record of our family travels. We already shipped it back once to add three new countries, and the new lines look as crisp as the first ones did on day one.</p>
  <div class="abs quote-name">JORDAN VALE</div>
  <div class="abs quote-role">TRAVELER</div>
</section>

<div class="abs tile tile-luggage" role="img" aria-label="Grey suitcases with luggage tags at an airport"><div class="tile-label"><b>CUSTOM</b> LUGGAGE TAG</div></div>
<div class="abs tile tile-sale">
  <div class="sale-title">15% OFF SALE</div>
  <div class="sale-rule"></div>
  <p class="sale-copy">Save on your first engraved luggage tag or passport wallet this month.</p>
  <a class="btn-blue">SHOP NOW</a>
</div>
<div class="abs tile tile-wallet-a" role="img" aria-label="Leather passport wallet with passport and cash on wood"><div class="tile-label"><b>PASSPORT</b> WALLET</div></div>
<div class="abs tile tile-wallet-b" role="img" aria-label="Travel flat lay with hat, map, camera and wallet"><div class="tile-label"><b>PASSPORT</b> WALLET</div></div>

<section class="related">
  <h2 class="abs section-title"><b>YOU MAY</b> ALSO LIKE</h2>
  <div class="abs rule" style="top:2614px"></div>
  <div class="abs related-card" style="left:108px">
    <div class="related-photo" role="img" aria-label="Suitcases with luggage tag" style="background:linear-gradient(120deg,#b8bcc2,#6c7178)"></div>
    <div class="related-name">ROAMSTEAD TAG</div><div class="related-price">$ 20.00</div>
  </div>
  <div class="abs related-card" style="left:442px">
    <div class="related-photo" role="img" aria-label="Two travel bottles outdoors" style="background:linear-gradient(120deg,#9db86e,#5d7d8e)"></div>
    <div class="related-name">ROAMSTEAD BOTTLE</div><div class="related-price">$ 20.00</div>
  </div>
  <div class="abs related-card" style="left:776px">
    <div class="related-photo" role="img" aria-label="Leather travel journal on wood" style="background:linear-gradient(120deg,#6b4a30,#3a2a1e)"></div>
    <div class="related-name">ROAMSTEAD JOURNAL</div><div class="related-price">$ 20.00</div>
  </div>
</section>

<footer class="abs site-footer">
  <div class="abs footer-col" style="left:108px"><h4>INFORMATION</h4>Shop<br>Setting<br>About Us<br>Register Your Tag</div>
  <div class="abs footer-col" style="left:340px"><h4>HELP</h4>FAQ<br>Terms &amp; Conditions<br>Contact Us</div>
  <div class="abs footer-col" style="left:548px"><h4>CONTACT US</h4>1234 Harbor Lane, Suite 8,<br>Portland OR 97201<br>+1 555 010 0000<br>hello@roamstead.example</div>
  <div class="abs footer-col" style="left:796px;width:296px"><h4>ABOUT US</h4>We engrave the places you have been and the places you will go on tags and wallets made to last.</div>
  <div class="abs footer-bottom">
    <div class="cards"><span class="card-chip"></span><span class="card-chip"></span><span class="card-chip"></span><span class="card-chip"></span></div>
    <span>© Copyright 2024 | Privacy policy</span>
  </div>
</footer>

</body>
</html>
```